Verdal Group Business Card Design

The CEO is looking for a new trendy look for his business card.
You can stay with current branding or come up with something new/creative. It can be 3D, including Medical Office buildings. You can use our logo in a variety of colors. Please include name, title, company name, company website, email address, cell number

Target Market(s)

Real Estate Development and Construction

Industry/Entity Type

Health care real estate

Contact Information for Business Card

Rohesh Kamble, CEO M-702.418.6293 E-roheshkamble@verdal.example Address:4100 Lanyard St, Tampa, FL 33611 www.verdal.example

Other font styles liked:
• Be creative

Requirements
Must have
• Creative, trendy look
Nice to have
• Please go to our website to get a feel- www. verdal.example
Should not have
• small fonts

```html
<!DOCTYPE html>
<html lang="en">
<head>
<meta charset="utf-8">
<title>Verdal Group Business Card</title>
<link rel="stylesheet" href="https://fonts.googleapis.com/css2?family=Arimo:wght@400;700&display=swap">
<style>
  :root {
    --bg: #e4e4e6;
    --card-dark: #2d2d2f;
    --card-light: #ffffff;
    --brand-red: #b01f2a;
    --brand-navy: #1b2a4a;
    --text-grey: #555a60;
    --divider: #c9cbce;
    --white: #ffffff;
  }
  * { box-sizing: border-box; margin: 0; padding: 0; }
  html, body { width: 1200px; height: 689px; overflow: hidden; }
  body {
    background: var(--bg);
    font-family: "Arimo", Arial, sans-serif;
    position: relative;
  }
  .card {
    position: absolute;
    top: 190px;
    width: 540px;
    height: 309px;
    border-radius: 16px;
    overflow: hidden;
    box-shadow: 0 10px 28px rgba(0,0,0,0.18);
  }
  .card--back { left: 40px; background: var(--card-dark); display: flex; align-items: center; justify-content: center; }
  .card--front { left: 620px; background: var(--card-light); }

  .brand-name {
    font-weight: 700;
    letter-spacing: -0.5px;
    line-height: 1;
  }
  .card--back .brand-name { color: var(--white); font-size: 52px; }
  .card--front .brand-name {
    position: absolute; left: 30px; top: 128px;
    color: var(--brand-red); font-size: 34px;
  }

  .divider {
    position: absolute; left: 262px; top: 48px;
    width: 1px; height: 150px; background: var(--divider);
  }
  .contact { position: absolute; left: 284px; top: 50px; }
  .contact__name { color: var(--brand-red); font-weight: 700; font-size: 22px; }
  .contact__title { color: var(--brand-navy); font-size: 14px; margin-top: 3px; }
  .contact__address { color: var(--text-grey); font-size: 14px; line-height: 1.3; margin-top: 16px; }
  .contact__lines { margin-top: 12px; }
  .contact__line {
    display: flex; align-items: center; gap: 8px;
    color: var(--text-grey); font-size: 14px; line-height: 1.45;
  }
  .contact__line svg { width: 12px; height: 12px; fill: var(--brand-red); flex: none; }

  .stripes { position: absolute; left: 0; bottom: 0; width: 540px; height: 70px; }
  .website {
    position: absolute; right: 22px; bottom: 12px;
    color: var(--white); font-size: 14px; line-height: 16px;
  }
</style>
</head>
<body>
  <section class="card card--back" aria-label="Card back">
    <span class="brand-name">Verdal Group</span>
  </section>

  <section class="card card--front" aria-label="Card front">
    <span class="brand-name">Verdal Group</span>
    <div class="divider"></div>
    <div class="contact">
      <p class="contact__name">Rohesh Kamble</p>
      <p class="contact__title">CEO</p>
      <p class="contact__address">4100 Lanyard St, Tampa<br>FL 33611</p>
      <div class="contact__lines">
        <p class="contact__line">
          <svg viewBox="0 0 24 24" aria-hidden="true"><path d="M6.6 10.8a15 15 0 0 0 6.6 6.6l2.2-2.2a1 1 0 0 1 1-.25 11.4 11.4 0 0 0 3.6.6 1 1 0 0 1 1 1V20a1 1 0 0 1-1 1A17 17 0 0 1 3 4a1 1 0 0 1 1-1h3.5a1 1 0 0 1 1 1c0 1.25.2 2.45.6 3.6a1 1 0 0 1-.25 1z"/></svg>
          702.418.6293
        </p>
        <p class="contact__line">
          <svg viewBox="0 0 24 24" aria-hidden="true"><path d="M2 5h20v14H2z M2 5l10 8 10-8" /></svg>
          roheshkamble@verdal.example
        </p>
      </div>
    </div>
    <svg class="stripes" viewBox="0 0 540 70" aria-hidden="true">
      <path d="M0 52 L290 52 Q302 52 308 44 L318 30 Q322 24 330 24 L340 24 L340 28 L330 28 Q325 28 322 33 L312 47 Q305 56 292 56 L0 56 Z" fill="var(--brand-navy)"/>
      <path d="M0 62 L302 62 Q314 62 320 54 L330 40 Q334 34 342 34 L540 34 L540 70 L0 70 Z" fill="var(--brand-red)"/>
    </svg>
    <span class="website">www.verdal.example</span>
  </section>
</body>
</html>
```